Commercial Loan Originator Business Card (CHANGE COLORS SCHEME)

CHANGE COLOR SCHEME - SAME DESIGN

Name Miranda Lestock
Title Commercial Loan Originator
Office (800) 641-2905 x68
Direct (240) 731-2264
Email gardenpath4life@mailbox.example

Name Dale Fenwick
Office (800) 641-2905 x70
Direct (410) 392-6058
Email d.fenwickhomes@mailbox.example

Name Gerald Winslow
Office (800) 641-2905 x71
Direct (215) 946-3021
Email g.winslow63@mailbox.example

Name Joan Mallory
Office (800) 641-2905 x
Direct (202) 518-4467
Email jmallory74@mailbox.example

Name Norah Velasco
Office (800) 641-2905 x72
Direct (240) 867-1152
Email capitalhomelending@mailbox.example

```html
<!DOCTYPE html>
<html lang="en">
<head>
<meta charset="utf-8">
<title>Gerald Winslow – Commercial Loan Originator</title>
<link rel="stylesheet" href="https://fonts.googleapis.com/css2?family=Montserrat:wght@400;500;700;800&display=swap">
<style>
  :root {
    --accent: #0e5552;
    --accent-soft: #c9a54a;
    --card: #fbfaf6;
    --ink: #2f3a3a;
    --backdrop: #dcdfdd;
    --photo-light: #9fb3ad;
    --photo-dark: #2e3f3d;
  }
  * { box-sizing: border-box; margin: 0; padding: 0; }
  html, body {
    width: 1200px; height: 788px; overflow: hidden;
    background: var(--backdrop);
    font-family: "Montserrat", Arial, sans-serif;
  }
  .card {
    position: absolute; left: 120px; top: 120px;
    width: 960px; height: 548px;
    background: var(--card);
    border-radius: 30px;
    overflow: hidden;
    box-shadow: 0 10px 30px rgba(0,0,0,0.18);
  }
  .accent-panel {
    position: absolute; top: 0; right: 0;
    width: 260px; height: 100%;
    background: var(--accent);
  }
  .portrait-frame {
    position: absolute; left: 548px; top: 108px;
    width: 332px; height: 332px; border-radius: 50%;
    border: 5px solid var(--accent);
    background: var(--card);
    padding: 9px;
  }
  .portrait {
    width: 100%; height: 100%; border-radius: 50%;
    background: radial-gradient(circle at 60% 40%, var(--photo-light) 0%, #5f7672 45%, var(--photo-dark) 100%);
  }
  .identity { position: absolute; left: 60px; top: 150px; }
  .name {
    font-weight: 800; font-size: 38px; letter-spacing: 0.5px;
    color: var(--accent); line-height: 1;
  }
  .title {
    margin-top: 8px; font-weight: 400; font-size: 21px;
    color: var(--ink);
  }
  .divider {
    width: 18px; height: 3px; background: var(--accent-soft);
    margin: 22px 0 20px;
  }
  .contacts { list-style: none; }
  .contacts li {
    display: flex; align-items: center; gap: 12px;
    font-size: 23px; font-weight: 500; color: var(--ink);
    height: 42px;
  }
  .contacts svg { width: 20px; height: 20px; fill: var(--accent); flex: none; }
</style>
</head>
<body>
  <div class="card">
    <div class="accent-panel"></div>
    <div class="portrait-frame">
      <div class="portrait" role="img" aria-label="Portrait photo of Gerald Winslow in a suit, city office window behind"></div>
    </div>
    <div class="identity">
      <h1 class="name">GERALD WINSLOW</h1>
      <p class="title">Commercial Loan Originator</p>
      <div class="divider"></div>
      <ul class="contacts">
        <li>
          <svg viewBox="0 0 24 24" aria-hidden="true"><path d="M6.6 10.8a15.1 15.1 0 0 0 6.6 6.6l2.2-2.2a1 1 0 0 1 1-.25 11.4 11.4 0 0 0 3.6.57 1 1 0 0 1 1 1V20a1 1 0 0 1-1 1A17 17 0 0 1 3 4a1 1 0 0 1 1-1h3.5a1 1 0 0 1 1 1c0 1.25.2 2.45.57 3.57a1 1 0 0 1-.25 1z"/></svg>
          (800) 641-2905 x71
        </li>
        <li>
          <svg viewBox="0 0 24 24" aria-hidden="true"><path d="M7 1h10a2 2 0 0 1 2 2v18a2 2 0 0 1-2 2H7a2 2 0 0 1-2-2V3a2 2 0 0 1 2-2zm0 3v14h10V4zm5 15.5a1.2 1.2 0 1 0 0 2.4 1.2 1.2 0 0 0 0-2.4z"/></svg>
          (215) 946-3021
        </li>
        <li>
          <svg viewBox="0 0 24 24" aria-hidden="true"><path d="M2 5h20v14H2zm2 2v.5l8 5.5 8-5.5V7zm0 2.9V17h16V9.9l-8 5.5z"/></svg>
          g.winslow63@mailbox.example
        </li>
      </ul>
    </div>
  </div>
</body>
</html>
```